Business Card Design Project

looking for a stylish and simple double sided business card.
I am an artist - specialising in fashion illustration, portraits and murals.
the front should be simply my name and tag:

D U R E S K
Living in colour

My preference is for a Black background with DURESK in red or embossed.
Living in colour in White or multi-coloured.

the back will have detail:

Personalised Art
Portraits, Murals, Fashion Illustration

0437 582 190
duresk@duresk.com.au
www.duresk.com.au

Target Market(s)

Adults that are based in western speaking countries who have an appreciation for art and design. Portraits and wall art
Business owners who may need personalised all art for their business space. Murals and personalised canvass.
People in the fashion industry, who may require fashion illustrations.

Industry/Entity Type

Fashion

Requirements
Must have
• BOLD but simple at the same time, timeless modern element to it.
Nice to have
• simple lettering
Should not have
• Not too busy or wordy,

```html
<!DOCTYPE html>
<html lang="en">
<head>
<meta charset="utf-8">
<title>Duresk – Business Card</title>
<link rel="stylesheet" href="https://fonts.googleapis.com/css2?family=Marcellus&family=Didact+Gothic&display=swap">
<style>
  :root {
    --page-bg: #ecebe8;
    --card-dark: #1b1a1c;
    --card-glow: #403f42;
    --magenta: #e2007f;
    --magenta-deep: #a2185c;
    --name-ink: #1e1a1d;
    --accent-pink: #e6407f;
    --text-light: #f2f2f2;
    --rule-light: rgba(255, 255, 255, 0.85);
  }
  * { box-sizing: border-box; margin: 0; padding: 0; }
  html, body {
    width: 1200px;
    height: 1000px;
    overflow: hidden;
    background: var(--page-bg);
  }
  .sheet {
    width: 1200px;
    height: 1000px;
    display: flex;
    flex-direction: column;
    align-items: center;
    justify-content: center;
    gap: 24px;
  }
  .card {
    position: relative;
    width: 760px;
    height: 440px;
    background: radial-gradient(ellipse 55% 65% at 52% 62%, var(--card-glow) 0%, #2a292b 55%, var(--card-dark) 100%);
    box-shadow: 0 6px 18px rgba(0, 0, 0, 0.25);
    overflow: hidden;
  }
  .colour-block {
    position: absolute;
    top: 0;
    background: radial-gradient(ellipse 60% 70% at 55% 35%, var(--magenta) 0%, #c60d72 45%, var(--magenta-deep) 100%);
    border-radius: 0 0 14px 14px;
  }
  .card--front .colour-block { left: 184px; width: 366px; height: 262px; }
  .card--back .colour-block { left: 210px; width: 360px; height: 136px; }

  .brand-name {
    position: absolute;
    left: 184px;
    width: 366px;
    top: 132px;
    text-align: center;
    font-family: "Marcellus", serif;
    font-size: 54px;
    letter-spacing: 0.28em;
    padding-left: 0.28em;
    color: var(--name-ink);
  }
  .tagline {
    position: absolute;
    left: 0;
    right: 0;
    top: 294px;
    padding-left: 60px;
    text-align: center;
    font-family: "Didact Gothic", sans-serif;
    font-size: 27px;
    letter-spacing: 0.2em;
    color: var(--text-light);
  }
  .rule {
    position: absolute;
    height: 2px;
    background: linear-gradient(90deg, transparent 0%, var(--rule-light) 45%, rgba(255,255,255,0.5) 75%, transparent 100%);
  }
  .card--front .rule { left: 220px; width: 340px; top: 344px; }

  .service-heading {
    position: absolute;
    left: 0;
    right: 0;
    top: 160px;
    text-align: center;
    font-family: "Marcellus", serif;
    font-size: 31px;
    letter-spacing: 0.16em;
    color: var(--accent-pink);
  }
  .service-list {
    position: absolute;
    left: 0;
    right: 0;
    top: 226px;
    display: flex;
    justify-content: center;
    gap: 30px;
    list-style: none;
    font-family: "Didact Gothic", sans-serif;
    font-size: 20px;
    letter-spacing: 0.03em;
    color: var(--text-light);
  }
  .card--back .rule { left: 220px; width: 350px; top: 264px; }

  .contact-row {
    position: absolute;
    left: 100px;
    right: 50px;
    bottom: 36px;
    display: flex;
    justify-content: space-between;
    align-items: baseline;
    font-family: "Didact Gothic", sans-serif;
    font-size: 19px;
    letter-spacing: 0.05em;
    color: var(--text-light);
  }
</style>
</head>
<body>
  <main class="sheet">
    <section class="card card--front" aria-label="Business card front">
      <div class="colour-block"></div>
      <h1 class="brand-name">DURESK</h1>
      <p class="tagline">Living in colour</p>
      <div class="rule"></div>
    </section>

    <section class="card card--back" aria-label="Business card back">
      <div class="colour-block"></div>
      <h2 class="service-heading">PERSONALISED ART</h2>
      <ul class="service-list">
        <li>.Portraits</li>
        <li>.Murals</li>
        <li>.Fashion Illustration</li>
      </ul>
      <div class="rule"></div>
      <address class="contact-row" style="font-style: normal;">
        <span class="contact-phone">0437 582 190</span>
        <span class="contact-email">duresk@duresk.com.au</span>
        <span class="contact-web">www.duresk.com.au</span>
      </address>
    </section>
  </main>
</body>
</html>
```